Stationery Design Project

I have recently had developed a logo for my new company Northwind Venture Partners -see logo attached.
I now need the following
1. Letterhead design as Word template
text needs to show the logo and then
Northwind Venture Partners Pty Ltd
ABN 83 402 615 294
Level 5, Harrow Building
17 Wexley Court
Carrowby Heights, NSW 2190
Tel: + 61(0)2 7314 2086
www.northwindventurepartners.example
dericp@northwindventurepartners.example
2. Business card -print ready -
Front side needs to show logo then text as follows
Deric Pellham
CEO
Level 5, Harrow Building
17 Wexley Court
Carrowby Heights, NSW 2190
T: + 61 (0)2 7314 2086
M: + 61 (0)438 772 104
dericp@brolvenco.example
On the back of the business card should appear the logo then text as follows
Correct text for the back of the card now in the attached word file please use bold and italics as indicated. Thanks
3. With compliments slip: Including logo + the web address www.northwindventurepartners.example
With compliments slip should fit 3 to an A4 sheet
4. Envelop design including logo + address
For the ethos of the company original brief for the logo below:
I am creating a new business advisory company called Northwind Venture Partners. the Web address will be www.northwindventurepartners.example This business is focused on assisting medium size businesses to achieve their growth objectives. The three pillars are self explanatory -it is focused on businesses that seek to build a global footprint, they seek to define/refine their business model and strategy, they are forward looking and focused on achieving growth.
The ethos of this company will be innovative thinking, passionate, dynamic, entrepreneurial this should reflected in the logo. That said the Logo should not be 'complicated' it should be simple and elegant...
Thanks Deric Pellham
Reason: I have been travelling all this week -so will only get a chance to review this weekend. Thanks
Target Market(s)
Medium sized business owners with sales between US$5m and $50m.
Industry/Entity Type
Business
Look and feel

```html
<!DOCTYPE html>
<html lang="en">
<head>
<meta charset="utf-8">
<title>Northwind Venture Partners – Business Card</title>
<link rel="stylesheet" href="https://fonts.googleapis.com/css2?family=Jost:wght@300;400;500&display=swap">
<style>
  :root {
    --backdrop: #ececec;
    --card: #ffffff;
    --ink: #2b2b2b;
    --brand-blue: #0a6ec2;
    --bar-blue: #0b3f9e;
    --mark-teal: #6fbfbd;
    --icon-blue: #1f4fa0;
    --rule-dark: #1f4fa0;
    --rule-light: #35c4ee;
  }
  * { box-sizing: border-box; margin: 0; padding: 0; }
  html, body { width: 1200px; height: 900px; overflow: hidden; }
  body {
    position: relative;
    background: var(--backdrop);
    font-family: "Jost", sans-serif;
    font-weight: 300;
    color: var(--ink);
  }
  .card {
    position: absolute;
    width: 533px;
    height: 295px;
    background: var(--card);
    box-shadow: 3px 4px 6px rgba(0,0,0,0.18);
  }
  .card--front { left: 153px; top: 120px; }
  .card--back  { left: 505px; top: 475px; width: 535px; }

  .brand {
    position: absolute;
    display: flex;
    align-items: center;
    gap: 12px;
  }
  .brand__square { width: 30px; height: 30px; background: var(--mark-teal); flex: none; }
  .brand__name {
    font-size: 35px;
    font-weight: 500;
    color: var(--brand-blue);
    white-space: nowrap;
    letter-spacing: -0.3px;
  }
  .card--front .brand { left: 19px; top: 24px; }
  .card--back .brand  { left: 18px; top: 22px; }

  .accent-bar {
    position: absolute;
    top: 122px;
    width: 12px;
    height: 45px;
    background: var(--bar-blue);
  }
  .accent-bar--left { left: 0; }
  .accent-bar--right { right: 0; }

  .person { position: absolute; left: 18px; top: 122px; line-height: 23px; }
  .person__name { font-size: 21px; }
  .person__role { font-size: 18px; }

  .website {
    position: absolute;
    right: 22px;
    top: 126px;
    font-size: 14px;
    white-space: nowrap;
  }

  .contacts {
    position: absolute;
    left: 20px;
    top: 199px;
    list-style: none;
    font-size: 15px;
    line-height: 19.5px;
  }
  .contacts li { display: flex; align-items: center; gap: 5px; }
  .contacts svg { width: 11px; height: 11px; fill: var(--icon-blue); flex: none; }

  .address {
    position: absolute;
    left: 305px;
    top: 201px;
    font-style: normal;
    font-size: 15px;
    line-height: 19.5px;
    white-space: nowrap;
  }

  .services {
    position: absolute;
    left: 17px;
    top: 95px;
    width: 500px;
    list-style: none;
    font-size: 17px;
  }
  .services li {
    position: relative;
    height: 32.4px;
    padding-left: 53px;
    line-height: 22px;
    white-space: nowrap;
  }
  .services li::before {
    content: "";
    position: absolute;
    left: 43px;
    top: 10px;
    width: 4px;
    height: 4px;
    border-radius: 50%;
    background: var(--ink);
  }
  .services li::after {
    content: "";
    position: absolute;
    left: 0;
    bottom: 0;
    width: 500px;
    height: 2px;
    background: linear-gradient(90deg, var(--rule-dark), var(--rule-light));
    -webkit-mask: repeating-linear-gradient(90deg, #000 0 2px, transparent 2px 4.6px);
    mask: repeating-linear-gradient(90deg, #000 0 2px, transparent 2px 4.6px);
  }
  .services li:last-child::after { display: none; }
</style>
</head>
<body>

<section class="card card--front" aria-label="Business card front">
  <div class="brand">
    <span class="brand__square"></span>
    <span class="brand__name">Northwind Venture Partners</span>
  </div>

  <span class="accent-bar accent-bar--left"></span>
  <span class="accent-bar accent-bar--right"></span>

  <div class="person">
    <p class="person__name">Deric Pellham</p>
    <p class="person__role">CEO</p>
  </div>

  <p class="website">www.northwindventurepartners.example</p>

  <ul class="contacts">
    <li>
      <svg viewBox="0 0 12 12" aria-hidden="true"><rect x="3" y="0.5" width="6" height="11" rx="1"/><rect x="4" y="2" width="4" height="4" fill="#fff"/></svg>
      + 61 438 772 104
    </li>
    <li>
      <svg viewBox="0 0 12 12" aria-hidden="true"><path d="M3 1 L5 1 L5.5 4 L4.2 5 Q5 7.3 7 8 L8 6.6 L11 7 L11 9 Q11 11 9 11 Q2 10 1 3 Q1 1 3 1Z"/></svg>
      + 61 (0)2 7314 2086
    </li>
    <li>
      <svg viewBox="0 0 12 12" aria-hidden="true"><rect x="3" y="0.5" width="6" height="3"/><rect x="0.5" y="4" width="11" height="5" rx="1"/><rect x="3" y="8" width="6" height="3.5"/></svg>
      + 61 (0)2 7390 5512
    </li>
    <li>
      <svg viewBox="0 0 12 12" aria-hidden="true"><rect x="0.5" y="2" width="11" height="8"/><path d="M0.5 2 L6 6.5 L11.5 2" stroke="#fff" stroke-width="1" fill="none"/></svg>
      dericp@brolvenco.example
    </li>
  </ul>

  <address class="address">
    Northwind Venture Partners Pty Ltd<br>
    Level 5, Harrow Building<br>
    17 Wexley Court<br>
    Carrowby Heights, NSW 2190
  </address>
</section>

<section class="card card--back" aria-label="Business card back">
  <div class="brand">
    <span class="brand__square"></span>
    <span class="brand__name">Northwind Venture Partners</span>
  </div>

  <ul class="services">
    <li>Develop the Right Strategy for your business</li>
    <li>Be accountable - create your Advisory Board</li>
    <li>Build a Business Plan your team will implement</li>
    <li>Take your business global - Export Market Development</li>
    <li>CEO groups</li>
    <li>Presentations, Seminars, Conferences</li>
  </ul>
</section>

</body>
</html>
```